U.S. based testing, inspection, and certification (TIC) company needs a new social media design.

We need a social media design primarily for LinkedIn 1200x1200px for our U.S. based company with international capabilities for performing dozens if not hundreds of testing, inspection, and certification (TIC) services. Our primary services include calibration, chemical analysis, consulting engineering, environmental simulation, forensic engineering, materials testing, mechanical testing, and nondestructive testing. Industries we serve are aerospace/aviation, automotive, chemical, commercial properties, construction, consumer products, defense, energy storage, healthcare, insurance/legal, life science, manufacturing, oil & gas, power generation, pulp & paper, and telecommunications. https://veltrolabs.example/

Guideline hex colors (primary, secondary): #29aae2, #0b1f3b

The final design should communicate:
1. Trust, Integrity, and Independence
2. Technical Expertise and Accuracy
3. Efficiency and Speed
4. Value-Added Partnership

We previously used a hexagon design that we would like to part ways from; hexagon examples and KRV logos uploaded.

```html
<!DOCTYPE html>
<html lang="en">
<head>
<meta charset="utf-8">
<title>KRV – Independent Results. Trusted Decisions.</title>
<link rel="stylesheet" href="https://fonts.googleapis.com/css2?family=Montserrat:wght@500;600;700&family=Inter:wght@400&display=swap">
<style>
  :root {
    --navy-deep: #0b1f3b;
    --navy-edge: #081628;
    --panel-top: #13345a;
    --panel-bottom: #0c2240;
    --brand-blue: #29aae2;
    --sky-text: #8fd6f4;
    --link-blue: #5cc0ef;
    --white: #ffffff;
    --streak: #6fd0ff;
  }
  * { margin: 0; padding: 0; box-sizing: border-box; }
  html, body { width: 1200px; height: 1200px; overflow: hidden; background: var(--navy-edge); }
  .social-post {
    position: relative;
    width: 1200px;
    height: 1200px;
    background: var(--navy-edge);
    font-family: "Montserrat", sans-serif;
    color: var(--white);
    overflow: hidden;
  }
  .inner-panel {
    position: absolute;
    left: 60px; top: 55px;
    width: 1090px; height: 1095px;
    background: radial-gradient(ellipse at 55% 25%, var(--panel-top) 0%, var(--panel-bottom) 60%, var(--navy-deep) 100%);
  }
  .backdrop { position: absolute; inset: 0; }
  .brand {
    position: absolute;
    top: 92px; left: 0; width: 1200px;
    text-align: center;
  }
  .brand-name {
    display: inline-flex; align-items: center; gap: 18px;
    font-size: 82px; font-weight: 700; letter-spacing: 6px;
    color: var(--brand-blue); line-height: 1;
  }
  .brand-mark { width: 22px; height: 22px; background: var(--brand-blue); }
  .brand-tagline {
    margin-top: 16px;
    font-family: "Inter", sans-serif;
    font-size: 27px; font-weight: 400;
    color: var(--white);
    padding-left: 10px;
  }
  .headline {
    position: absolute; left: 132px; top: 296px;
    font-size: 64px; font-weight: 600; line-height: 76px;
    letter-spacing: 0.5px;
  }
  .subhead {
    position: absolute; left: 132px; top: 478px;
    font-size: 34px; font-weight: 500;
    color: var(--sky-text);
  }
  .benefits {
    position: absolute; left: 132px; top: 562px;
    list-style: none;
  }
  .benefits li {
    display: flex; align-items: center; gap: 20px;
    font-size: 30px; font-weight: 500; height: 55px;
  }
  .benefits svg { width: 30px; height: 30px; }
  .site-link {
    position: absolute; left: 138px; top: 770px;
    font-size: 30px; font-weight: 600; color: var(--link-blue);
  }
</style>
</head>
<body>
<main class="social-post">
  <div class="inner-panel"></div>

  <svg class="backdrop" width="1200" height="1200" viewBox="0 0 1200 1200">
    <defs>
      <linearGradient id="labPhotoTone" x1="0" y1="0" x2="1" y2="1">
        <stop offset="0" stop-color="#1b3f66"/>
        <stop offset="0.5" stop-color="#34506e"/>
        <stop offset="1" stop-color="#1a2c44"/>
      </linearGradient>
      <linearGradient id="streakGlow" x1="0" y1="1" x2="1" y2="0">
        <stop offset="0" stop-color="#29aae2" stop-opacity="0.2"/>
        <stop offset="0.6" stop-color="#6fd0ff" stop-opacity="0.9"/>
        <stop offset="1" stop-color="#bfeaff" stop-opacity="1"/>
      </linearGradient>
    </defs>
    <g stroke="#2a5a86" stroke-opacity="0.35" fill="none">
      <line x1="60" y1="470" x2="1000" y2="470"/>
      <line x1="60" y1="528" x2="900" y2="528"/>
      <line x1="60" y1="750" x2="720" y2="750"/>
      <rect x="510" y="570" width="240" height="180"/>
    </g>
    <polygon class="lab-photo" role="img"
      aria-label="Photo of a technician's hand probing cables into a digital oscilloscope and test instruments in a laboratory"
      points="1150,215 1150,1150 262,1150" fill="url(#labPhotoTone)"/>
    <line x1="240" y1="1150" x2="1150" y2="200" stroke="url(#streakGlow)" stroke-width="4"/>
    <line x1="262" y1="1150" x2="1150" y2="225" stroke="#29aae2" stroke-opacity="0.45" stroke-width="2"/>
  </svg>

  <header class="brand">
    <div class="brand-name"><span class="brand-mark"></span>KRV</div>
    <p class="brand-tagline">Korvane Technical Services</p>
  </header>

  <h1 class="headline">Independent Results.<br>Trusted Decisions.</h1>
  <p class="subhead">TIC Services for Critical Industries</p>

  <ul class="benefits">
    <li><svg viewBox="0 0 30 30"><path d="M3 16 L11 24 L27 6" fill="none" stroke="#29aae2" stroke-width="3" stroke-linecap="round" stroke-linejoin="round"/></svg>Precise</li>
    <li><svg viewBox="0 0 30 30"><path d="M3 16 L11 24 L27 6" fill="none" stroke="#29aae2" stroke-width="3" stroke-linecap="round" stroke-linejoin="round"/></svg>Independent</li>
    <li><svg viewBox="0 0 30 30"><path d="M3 16 L11 24 L27 6" fill="none" stroke="#29aae2" stroke-width="3" stroke-linecap="round" stroke-linejoin="round"/></svg>Responsive</li>
  </ul>

  <p class="site-link">veltrolabs.example</p>
</main>
</body>
</html>
```